Thimble Nook web site

I have been running an online business for 6 years.
www.thimblenook.com.au I specialise in ribbons, buttons and unique craft materials. I sell online to individuals and shops with seperate retail and wholesale sites. The web page I'd like redesigned is my retail site.

It needs a clean, fresh look. I've recently had a new logo designed (thanks pixel harbour!) and want the web site to incorporate the new design and colour scheme of black and white. (new logo attached as a file)

I no longer want the page with the large image www.thimblenook.com.au I want to have the first page as the retail shop homepage.
http://www.thimblenook.com.au/index.php so this page needs to have all the links

I want to the look to be fresh, modern and clear. It needs to be quick to load.

Notes from my IT guru: They need to know that the following tend to remain static with just the content section changing on each page; Header Left column (but different in the cart) right column (if required) footer
Updates

Thanks for your designs. 1/3 of my users use mobile devices so please take that into consideration. I would like the logo to be incorporated into the design and be a prominent feature (most have just used it as a tiny image in the top left corner. I would like it to be larger and more prominent.  thanks                                   

Thanks to all the designers who have submitted. Can you please add  'Boutique craft supplies' near the logo. That is my tag line. Thanks

Target Market(s)

Crafty females of all ages

Industry/Entity Type

Business

Requirements
Must have
• links to;
blog
gallery
chatterloop
snapboardly
wholesale
space for an image which I change approx every 2 weeks
about Thimble Nook
contact
privacy policy
terms and conditions
newsletter sign up
shipping info
product search
Nice to have
• I am not sure if I want product images on the homepage? I have attached a few images.
Should not have
• not too much colour - I hate the green border I have now

```html
<!DOCTYPE html>
<html lang="en">
<head>
<meta charset="utf-8">
<title>Thimble Nook – Boutique Craft Supplies</title>
<link href="https://fonts.googleapis.com/css2?family=Roboto+Slab:wght@300;400;700;800&family=Carlito&display=swap" rel="stylesheet">
<style>
:root{
  --purple:#7b1c9c;
  --purple-dark:#55106d;
  --purple-light:#9b3bbd;
  --ink:#111;
  --text:#333;
  --muted:#777;
  --page:#e9e9e9;
  --stripe:#dedede;
  --panel:#000;
  --white:#fff;
  --rule:#c9c9c9;
}
*{box-sizing:border-box;margin:0;padding:0}
html,body{width:1200px;height:1005px;overflow:hidden}
body{
  position:relative;
  font-family:"Carlito",sans-serif;
  color:var(--text);
  background:
    radial-gradient(ellipse at 50% 55%,rgba(255,255,255,.85),rgba(255,255,255,0) 60%),
    repeating-linear-gradient(90deg,var(--page) 0 38px,var(--stripe) 38px 76px);
}
.top-notice{position:absolute;top:15px;left:0;width:1200px;text-align:center;
  font:300 13px "Roboto Slab",serif;color:#666}
.top-notice::before{content:"";position:absolute;left:0;right:0;top:-13px;border-top:2px dotted #bbb}

/* navigation ribbon */
.nav-tail{position:absolute;top:155px;width:60px;height:46px;background:var(--purple-dark)}
.nav-tail.left{left:111px;clip-path:polygon(0 50%,12% 20%,100% 0,100% 100%,12% 80%)}
.nav-tail.right{right:111px;clip-path:polygon(100% 50%,88% 20%,0 0,0 100%,88% 80%)}
.nav-band{position:absolute;top:141px;height:45px;background:linear-gradient(var(--purple-light),var(--purple) 45%,var(--purple-dark));
  border:3px solid var(--purple-dark);box-shadow:inset 0 0 0 2px rgba(255,255,255,.15);display:flex;align-items:center}
.nav-band.left{left:159px;width:330px;padding-left:43px;gap:0}
.nav-band.right{left:712px;width:328px;justify-content:flex-end;padding-right:14px}
.nav-band a{font:400 17px "Roboto Slab",serif;color:var(--white);text-decoration:none}
.nav-band.left a{margin-right:38px}
.nav-band.right a{margin-left:30px}
.nav-band a.current{background:var(--ink);padding:3px 13px;margin-left:-13px;margin-right:25px}

/* brand */
.brand{position:absolute;left:476px;top:95px;width:250px;text-align:center}
.brand-name{font:700 37px "Roboto Slab",serif;color:var(--ink);line-height:1}
.tagline{position:absolute;left:476px;top:209px;width:250px;text-align:center;
  font:300 13px "Carlito",sans-serif;letter-spacing:1.5px;color:#555}

/* social */
.social{position:absolute;left:202px;top:222px;display:flex;gap:12px}
.social a{display:flex;align-items:center;gap:4px;font:400 13px "Carlito",sans-serif;color:var(--ink);text-decoration:none}
.social a::before{content:"";width:12px;height:12px;border-radius:50%;background:var(--ink)}

/* search */
.search{position:absolute;left:739px;top:218px;width:258px;height:29px;border:1px dashed #aaa;background:rgba(255,255,255,.6);display:flex;align-items:center}
.search svg{margin:0 7px 0 8px}
.search span{border-left:1px solid #bbb;padding-left:10px;font:400 13px "Carlito",sans-serif;color:#222;letter-spacing:.3px}

/* feature banner */
.feature{position:absolute;left:189px;top:272px;width:822px;height:259px;border:1px dashed #a98ac4;
  background:linear-gradient(160deg,#f1eef4 0%,#d9c8ec 35%,#ecd8e6 55%,#e6efcf 75%,#f2f2f2 100%);
  box-shadow:0 12px 14px -10px rgba(0,0,0,.35)}
.feature-copy{position:absolute;right:32px;bottom:32px;font-family:"Roboto Slab",serif;color:var(--ink);line-height:.92;
  text-shadow:1px 1px 0 #fff}
.feature-copy .small{display:block;font-weight:700;font-size:21px}
.feature-copy .big{display:block;font-weight:800;font-size:36px;letter-spacing:-1px}

/* categories */
.categories-title{position:absolute;left:198px;top:565px;font:700 24px "Roboto Slab",serif;color:var(--ink);letter-spacing:-.5px}
.category-grid{position:absolute;left:192px;top:608px;display:grid;
  grid-template-columns:110px 118px 128px 124px 157px 98px 80px;grid-auto-rows:29px;column-gap:0}
.category-grid a{font:400 13px "Carlito",sans-serif;color:#222;text-decoration:none;display:flex;align-items:center;
  padding-left:5px;margin-right:12px;border-bottom:1px dotted var(--rule);position:relative}
.category-grid a::after{content:"";position:absolute;right:-7px;top:2px;bottom:2px;border-right:1px dotted var(--rule)}
.category-grid a:nth-child(7n)::after{display:none}

/* black info panel */
.panel-fold{position:absolute;top:748px;width:28px;height:186px;background:#333}
.panel-fold.left{left:159px;clip-path:polygon(0 6%,100% 0,100% 100%,0 94%)}
.panel-fold.right{left:1012px;clip-path:polygon(0 0,100% 6%,100% 94%,0 100%)}
.info-panel{position:absolute;left:159px;top:759px;width:881px;height:162px;background:var(--panel);
  outline:1px dashed #555;outline-offset:-7px;color:var(--white)}
.info-panel h2{position:absolute;top:19px;font:400 24px "Roboto Slab",serif;letter-spacing:-.5px}
.divider{position:absolute;top:18px;bottom:18px;border-left:1px dotted #666}
.product-thumb{position:absolute;left:33px;top:54px;width:106px;height:80px;border:2px solid #888;
  background:linear-gradient(135deg,#cde6c8,#a8d29c 50%,#d6e8d8)}
.product-name{position:absolute;left:149px;top:56px;font:300 15px "Roboto Slab",serif;line-height:1.15;color:#ddd}
.product-price{position:absolute;left:149px;top:98px;font:400 37px "Roboto Slab",serif;letter-spacing:-1px}
.mailing-note{position:absolute;left:391px;top:56px;font:300 12px "Roboto Slab",serif;color:#ddd}
.email-field{position:absolute;left:390px;top:73px;width:245px;height:27px;background:var(--white);color:#222;
  font:400 13px "Roboto Slab",serif;padding:5px 8px}
.subscribe{position:absolute;left:390px;top:105px;width:109px;height:30px;background:var(--purple);
  font:400 13px "Roboto Slab",serif;color:var(--white);display:flex;align-items:center;justify-content:center}
.cart-icon{position:absolute;left:678px;top:64px}
.cart-count{position:absolute;left:726px;top:72px;font:300 27px "Roboto Slab",serif;letter-spacing:-1px}
.cart-count em{font-style:normal;color:var(--purple-light)}
.cart-note{position:absolute;left:683px;top:117px;font:300 13px "Roboto Slab",serif;color:#ddd}

/* footer */
.footer-links{position:absolute;top:942px;left:0;width:1200px;text-align:center;font:400 12.5px "Roboto Slab",serif;color:var(--ink)}
.footer-links a{color:var(--ink);text-decoration:none}
.footer-links .sep{margin:0 5px}
.copyright{position:absolute;top:964px;left:0;width:1200px;text-align:center;font:300 12px "Roboto Slab",serif;color:var(--muted)}
</style>
</head>
<body>

<p class="top-notice">Visit us at the Riverside Craft &amp; Quilt Fair 22-26th May, Riverside Exhibition Hall STAND G32</p>

<div class="nav-tail left"></div>
<div class="nav-tail right"></div>
<nav class="nav-band left">
  <a class="current" href="#">Home</a>
  <a href="#">Wholesale</a>
  <a href="#">Gallery</a>
</nav>
<nav class="nav-band right">
  <a href="#">About Thimble Nook</a>
  <a href="#">Blog</a>
  <a href="#">Contact</a>
</nav>

<header class="brand"><div class="brand-name">Thimble Nook</div></header>
<p class="tagline">Boutique Craft Supplies</p>

<div class="social">
  <a href="#">snapboardly</a>
  <a href="#">chatterloop</a>
</div>

<div class="search">
  <svg width="18" height="18" viewBox="0 0 18 18"><circle cx="7" cy="7" r="5" fill="none" stroke="#999" stroke-width="2"/><line x1="11" y1="11" x2="16" y2="16" stroke="#999" stroke-width="2.5" stroke-linecap="round"/></svg>
  <span>ENTER YOUR KEYWORDS HERE</span>
</div>

<section class="feature" role="img" aria-label="Photo of pastel gingham ribbons in purple, pink, green and yellow with a pink satin bow">
  <div class="feature-copy"><span class="small">SPECIALIZING IN</span><span class="big">UNIQUE RIBBONS</span></div>
</section>

<h2 class="categories-title">CATEGORIES</h2>
<div class="category-grid">
  <a href="#">New Products</a><a href="#">** Clearance **</a><a href="#">Adhesives</a><a href="#">Buttons</a><a href="#">Card Kits</a><a href="#">Charms</a><a href="#">Chipboard</a>
  <a href="#">Christmas</a><a href="#">Embellishments</a><a href="#">Embossing Folders</a><a href="#">Flowers &amp; Leaves</a><a href="#">Inks, Mists And Masks</a><a href="#">Lace</a><a href="#">Miscellaneous</a>
  <a href="#">Paper</a><a href="#">Ribbon Club</a><a href="#">Ribbons</a><a href="#">Ribbons - organza</a><a href="#">Ric Rac</a><a href="#">Sequins</a><a href="#">Stamps</a>
  <a href="#">Stickers</a><a href="#">Washi tape</a>
</div>

<div class="panel-fold left"></div>
<div class="panel-fold right"></div>
<section class="info-panel">
  <h2 style="left:32px">Latest Products</h2>
  <div class="product-thumb" role="img" aria-label="Product photo of a green ribbon printed with cars, helicopters and trucks"></div>
  <p class="product-name">Transport Ribbon - Car,<br>Helicopter &amp; Truck</p>
  <p class="product-price">$2.50</p>

  <div class="divider" style="left:375px"></div>
  <h2 style="left:391px">Mailing List</h2>
  <p class="mailing-note">Subscribe to our mailing list below:</p>
  <div class="email-field">Enter Your Email Address</div>
  <div class="subscribe">Subscribe</div>

  <div class="divider" style="left:647px"></div>
  <h2 style="left:675px">Shopping Cart</h2>
  <svg class="cart-icon" width="40" height="44" viewBox="0 0 40 44">
    <path d="M12 16 L20 3 L28 16" fill="none" stroke="#fff" stroke-width="2.5"/>
    <rect x="2" y="15" width="36" height="6" fill="#fff"/>
    <path d="M5 23 H35 L32 42 H8 Z" fill="none" stroke="#fff" stroke-width="2.5"/>
    <path d="M11 26 V38 M15 26 V38 M20 26 V38 M25 26 V38 M29 26 V38" stroke="#fff" stroke-width="2"/>
  </svg>
  <p class="cart-count">0 <em>Items</em></p>
  <p class="cart-note">Your Cart Is Empty Now!</p>
</section>

<footer>
  <p class="footer-links"><a href="#">About Thimble Nook</a><span class="sep">|</span><a href="#">Contact Thimble Nook</a><span class="sep">|</span><a href="#">Privacy Policy</a><span class="sep">|</span><a href="#">Terms &amp; Conditions</a></p>
  <p class="copyright">© 2013 ThimbleNook.com.au. All rights reserved.</p>
</footer>

</body>
</html>
```